New Business Card Design Project

We would like a business card that represents the sale of boat, home, auto, and life insurance.

The logo can change colors to meet the look of the design if needed.

Industry/Entity Type

Business

```html
<!DOCTYPE html>
<html lang="en">
<head>
<meta charset="utf-8">
<title>Vantor Financial – Business Card</title>
<link rel="stylesheet" href="https://fonts.googleapis.com/css2?family=Didact+Gothic&display=swap">
<style>
  :root {
    --page-bg: #e6e1da;
    --card-black: #151515;
    --card-black-light: #2c2c2c;
    --card-white: #ffffff;
    --panel-grey: #eeeeee;
    --brand-red: #d3263f;
    --tab-red: #e0485c;
    --text-dark: #4a4a4a;
    --text-light: #ffffff;
    --font-main: "Didact Gothic", "Century Gothic", sans-serif;
  }
  * { box-sizing: border-box; margin: 0; padding: 0; }
  html, body {
    width: 1200px; height: 1023px; overflow: hidden;
    background: var(--page-bg);
    font-family: var(--font-main);
  }
  .stage { position: relative; width: 1200px; height: 1023px; }

  .card {
    position: absolute;
    width: 600px; height: 343px;
    border-radius: 4px;
    overflow: hidden;
    box-shadow: 0 10px 28px rgba(0,0,0,.28);
  }

  /* Front */
  .card-front { left: 130px; top: 110px; background: var(--card-black); }
  .front-dark {
    position: absolute; inset: 0 0 140px 0;
    background: linear-gradient(160deg, var(--card-black-light) 0%, var(--card-black) 70%);
  }
  .front-panel {
    position: absolute; left: 0; right: 0; bottom: 12px; height: 128px;
    background: linear-gradient(180deg, var(--panel-grey) 0%, var(--card-white) 18%);
  }
  .front-edge {
    position: absolute; left: 0; right: 0; bottom: 0; height: 12px;
    background: var(--brand-red);
  }
  .front-brand {
    position: absolute; right: 30px; top: 38px; text-align: right;
    color: var(--text-light);
  }
  .brand-name {
    display: flex; align-items: center; justify-content: flex-end; gap: 12px;
    font-size: 34px; letter-spacing: 4px; line-height: 1;
  }
  .brand-dot {
    width: 22px; height: 22px; border-radius: 50%; background: var(--brand-red); flex: none;
  }
  .brand-tagline { margin-top: 10px; font-size: 19px; letter-spacing: .5px; }

  .name-tab {
    position: absolute; left: 0; top: 160px; width: 190px; height: 64px;
    background: var(--tab-red);
    border-radius: 0 12px 12px 0;
    color: var(--text-light);
    padding: 8px 0 0 22px;
  }
  .person-name { font-size: 24px; line-height: 1.1; }
  .person-role { font-size: 14px; margin-top: 2px; }

  .contact {
    position: absolute; left: 216px; top: 232px; right: 20px;
    color: var(--text-dark); font-size: 13px;
    display: grid; grid-template-columns: 150px 1fr; row-gap: 8px; column-gap: 16px;
  }
  .contact-item { display: flex; align-items: center; gap: 7px; white-space: nowrap; }
  .contact-address { grid-column: 1 / 3; padding-left: 21px; margin-top: -4px; }
  .accent { color: var(--brand-red); }
  .icon { width: 14px; height: 14px; flex: none; }

  /* Back */
  .card-back {
    left: 470px; top: 560px;
    background: linear-gradient(160deg, var(--card-black-light) 0%, var(--card-black) 65%);
  }
  .back-brand {
    position: absolute; left: 0; right: 0; top: 120px; text-align: center;
    color: var(--text-light);
  }
  .back-brand .brand-name { justify-content: center; font-size: 42px; }
  .back-brand .brand-tagline { font-size: 22px; }
</style>
</head>
<body>
<div class="stage">

  <section class="card card-front" aria-label="Business card front">
    <div class="front-dark"></div>
    <div class="front-panel"></div>
    <div class="front-edge"></div>

    <div class="front-brand">
      <div class="brand-name"><span class="brand-dot"></span>VANTOR FINANCIAL</div>
      <div class="brand-tagline">investments &amp; insurance</div>
    </div>

    <div class="name-tab">
      <div class="person-name">Your Name</div>
      <div class="person-role">Your Position</div>
    </div>

    <div class="contact">
      <div class="contact-item">
        <svg class="icon" viewBox="0 0 14 14"><rect width="14" height="14" rx="2" fill="#d3263f"/><path d="M4 3.5h2l.6 2-1.2.8a5 5 0 0 0 2.3 2.3l.8-1.2 2 .6v2a1 1 0 0 1-1 1A7 7 0 0 1 3 4.5a1 1 0 0 1 1-1z" fill="#fff"/></svg>
        0123 456 789
      </div>
      <div class="contact-item">
        <svg class="icon" viewBox="0 0 14 14"><rect width="14" height="14" rx="2" fill="#d3263f"/><rect x="3" y="4" width="8" height="6" fill="#fff"/><path d="M3 4l4 3.2L11 4" stroke="#d3263f" fill="none"/></svg>
        yourmail@<span class="accent">vantor</span>financial.com
      </div>
      <div class="contact-item">
        <svg class="icon" viewBox="0 0 14 14"><rect width="14" height="14" rx="2" fill="#d3263f"/><rect x="4.5" y="2.5" width="5" height="9" rx="1" fill="#fff"/></svg>
        0123 456 789
      </div>
      <div class="contact-item">
        <svg class="icon" viewBox="0 0 14 14"><rect width="14" height="14" rx="2" fill="#d3263f"/><circle cx="7" cy="7" r="4" fill="none" stroke="#fff"/><path d="M3 7h8M7 3v8" stroke="#fff"/></svg>
        www.<span class="accent">vantor</span>financial.com
      </div>
      <div class="contact-item" style="grid-column: 1 / 3;">
        <svg class="icon" viewBox="0 0 14 14"><rect width="14" height="14" rx="2" fill="#d3263f"/><path d="M7 2.5a3 3 0 0 1 3 3c0 2.2-3 6-3 6s-3-3.8-3-6a3 3 0 0 1 3-3z" fill="#fff"/><circle cx="7" cy="5.5" r="1" fill="#d3263f"/></svg>
        <span><span class="accent">Vantor</span> Financial Address:</span>
      </div>
      <div class="contact-address">1100 Unknown Street, Any where, Any City</div>
    </div>
  </section>

  <section class="card card-back" aria-label="Business card back">
    <div class="back-brand">
      <div class="brand-name"><span class="brand-dot"></span>VANTOR FINANCIAL</div>
      <div class="brand-tagline">investments &amp; insurance</div>
    </div>
  </section>

</div>
</body>
</html>
```